HOT TUB - SPAS service needs an business card

I need an business for my company who his specialise in a maintenance,water treatment and cleaning of Hot Tub - Spas for commercial and residential customers. The company operate mainly in the ski resort of Chamonix, Megève and St Gervais. The final product should communicate pure water, cleanest and professional for luxury property's.
I have upload a logo but any improvement on it is welcome.(color,size, details etc..) or any other idea. Thank you
Company Name: 58 BAINS
My name: Laurent Mazeyrac
Email: lmazey@courrielo.fr
Tel: +33 (0)6 81 52 29 07
Description to be on the card in french(first langage) and in English:
- Spas service
- Entretien, traitement eau, nettoyage.
- Maintenance, water treatment, cleaning.

```html
<!DOCTYPE html>
<html lang="fr">
<head>
<meta charset="utf-8">
<title>58 BAINS – cartes de visite</title>
<link href="https://fonts.googleapis.com/css2?family=Source+Sans+3:wght@400;600&display=swap" rel="stylesheet">
<style>
  :root {
    --page: #eceef0;
    --card-light: #f3f6f9;
    --brand-blue: #2a98e6;
    --card-blue: #0f78d9;
    --ink: #2b2b2b;
    --white: #ffffff;
    --water-a: #e3ebf2;
    --water-b: #c3d1de;
  }
  * { margin: 0; padding: 0; box-sizing: border-box; }
  html, body { width: 1200px; height: 1084px; overflow: hidden; }
  body {
    background: var(--page);
    font-family: "Source Sans 3", "Myriad Pro", Arial, sans-serif;
    position: relative;
  }
  .card {
    position: absolute;
    width: 850px;
    height: 484px;
    overflow: hidden;
    box-shadow: 0 4px 14px rgba(0,0,0,0.18);
  }
  .card--front { left: 34px; top: 30px; background: linear-gradient(180deg, #f7f9fb 0%, var(--card-light) 60%, #e8eef4 100%); }
  .card--back { left: 299px; top: 541px; background: var(--card-blue); color: var(--white); }

  .water-band {
    position: absolute;
    left: 0; top: 180px;
    width: 850px; height: 200px;
  }
  .brand {
    position: absolute;
    left: 0; right: 0;
    display: flex;
    justify-content: center;
    align-items: center;
    gap: 16px;
    font-weight: 600;
    letter-spacing: 1px;
  }
  .brand__dot {
    width: 18px; height: 18px; border-radius: 50%;
    background: currentColor;
  }
  .card--front .brand { top: 72px; padding-left: 60px; font-size: 64px; color: var(--brand-blue); }
  .card--back .brand { top: 140px; padding-left: 60px; font-size: 64px; }

  .holder {
    position: absolute; left: 0; right: 0; top: 346px;
    text-align: center; font-weight: 600; font-size: 37px; color: var(--brand-blue);
  }
  .contacts {
    position: absolute; left: 0; right: 0; top: 412px;
    display: flex; justify-content: center; gap: 24px;
    font-size: 28px; font-weight: 600; color: var(--ink);
  }
  .contacts__item { display: flex; align-items: center; gap: 10px; }
  .contacts__item svg { width: 24px; height: 24px; }

  .services {
    position: absolute; left: 0; right: 0; top: 333px; text-align: center;
  }
  .services__title { font-weight: 600; font-size: 32px; margin-bottom: 6px; }
  .services__line { font-size: 31px; line-height: 41px; }
</style>
</head>
<body>
  <section class="card card--front">
    <svg class="water-band" viewBox="0 0 850 200" role="img" aria-label="Vague d'eau claire avec bulles">
      <defs>
        <linearGradient id="waterFill" x1="0" y1="0" x2="1" y2="0">
          <stop offset="0" stop-color="#c9d6e2" stop-opacity="0.7"/>
          <stop offset="0.5" stop-color="#b4c5d5" stop-opacity="0.9"/>
          <stop offset="1" stop-color="#d4dfe9" stop-opacity="0.6"/>
        </linearGradient>
      </defs>
      <path d="M0 90 C120 130 220 170 340 140 C460 110 520 60 640 45 C740 32 810 40 850 30 L850 80 C790 90 730 80 640 100 C520 130 460 175 340 185 C220 195 110 160 0 130 Z" fill="url(#waterFill)"/>
    </svg>
    <div class="brand"><span class="brand__name">58 BAINS</span><span class="brand__dot"></span></div>
    <p class="holder">Laurent Mazeyrac</p>
    <div class="contacts">
      <span class="contacts__item">
        <svg viewBox="0 0 24 24" aria-hidden="true"><circle cx="12" cy="12" r="10.5" fill="none" stroke="#2b2b2b" stroke-width="1.5"/><path d="M8.5 6.5l2 2-1.2 1.5c.8 1.8 2 3 3.7 3.7l1.5-1.2 2 2-1.3 1.8c-3.8-.4-7.2-3.8-7.6-7.6z" fill="#2b2b2b"/></svg>
        +33 (0)6 81 52 29 07
      </span>
      <span class="contacts__item">
        <svg viewBox="0 0 24 24" aria-hidden="true"><path d="M2 10l10-7 10 7v11H2z" fill="#2b2b2b"/><path d="M2 10l10 6 10-6" fill="none" stroke="#fff" stroke-width="1.4"/><rect x="7" y="7" width="10" height="5" fill="#fff"/></svg>
        lmazey@courrielo.fr
      </span>
    </div>
  </section>

  <section class="card card--back">
    <div class="brand"><span class="brand__name">58 BAINS</span><span class="brand__dot"></span></div>
    <div class="services">
      <p class="services__title">SPAS SERVICES</p>
      <p class="services__line">• Entretien &nbsp;• traitement eau &nbsp;• nettoyage</p>
      <p class="services__line">• Maintenance &nbsp;• water treatment &nbsp;• cleaning.</p>
    </div>
  </section>
</body>
</html>
```